Create Stationary from existing logo(s)

We are looking for some assistance in tidying up the stationary that supports our brand. We are an innovative technology company, generally working with larger corporates. We have previously done a little work on brochures etc, but never really pulled it all together with our stationary.
In particular I am looking for:
1. A4 Letter Template for Letter (Microsoft Word 2007 template format)
2. A4 Template for Reports (Microsoft Word 2007 template format). This should include title page, table of contents, subsequent report pages including styles for tables, headings, and text.
3. Business Card Design - we will need to be able to edit the text, so the card should include sample text for name, title, phone number, mobile number, and email address.
4. Presentation Template (Microsoft Powerpoint 2007 template). See attached powerpoint which we quite like, but isn't really a template, and we have don't really use any consistent styles in it. The Powerpoint template needs to have a cover / title page, section break pages, and pages that may contain bullet point text, pictures, or a combination of bullet point text and pictures. We do like our current presentation, which gives some indication of our thinking.
I am attaching a brochure and the powerpoint presentation to give some indication of current materials. We are happy with the main concepts behind the brochure, and would not really be looking to change the key concepts unless you have a compelling reason. We do like the use of this secondary logo in the stationary related items
I have uploaded an eps file of the logo.

```html
<!DOCTYPE html>
<html lang="en">
<head>
<meta charset="utf-8">
<title>Meridian Systems Letterhead</title>
<link rel="stylesheet" href="https://fonts.googleapis.com/css2?family=Arimo:wght@400;700&display=swap">
<style>
  :root {
    --paper: #ffffff;
    --navy: #1d4f7c;
    --orange: #f39a2e;
    --blue-deep: #1f7fc4;
    --blue-mid: #5aaee0;
    --blue-pale: #cfe6f6;
    --ink: #555a60;
    --panel: rgba(255, 255, 255, 0.35);
  }
  html, body {
    margin: 0;
    padding: 0;
    overflow: hidden;
    background: var(--paper);
  }
  .letterhead {
    position: relative;
    width: 848px;
    height: 1200px;
    background: var(--paper);
    overflow: hidden;
    font-family: "Arimo", Arial, sans-serif;
  }
  .brand {
    position: absolute;
    top: 62px;
    right: 64px;
    display: flex;
    align-items: center;
    gap: 12px;
  }
  .brand-mark {
    width: 34px;
    height: 34px;
    background: var(--orange);
  }
  .brand-name {
    font-size: 27px;
    font-weight: 700;
    color: var(--navy);
    letter-spacing: -0.2px;
  }
  .footer-band {
    position: absolute;
    left: 0;
    bottom: 0;
    width: 848px;
    height: 180px;
    background:
      radial-gradient(circle at 48px 60px, rgba(243, 154, 46, 0.55) 0 34px, transparent 35px),
      radial-gradient(circle at 155px 55px, rgba(243, 154, 46, 0.45) 0 19px, transparent 20px),
      linear-gradient(172deg, transparent 0 18%, var(--blue-pale) 30%, var(--blue-mid) 60%, var(--blue-deep) 100%);
  }
  .contact-panel {
    position: absolute;
    left: 392px;
    top: 1079px;
    width: 413px;
    height: 83px;
    border-radius: 8px;
    background: var(--panel);
    display: flex;
    gap: 62px;
    padding: 12px 0 0 18px;
    box-sizing: border-box;
  }
  .contact-list {
    margin: 0;
    padding: 0;
    list-style: none;
    font-size: 11.5px;
    line-height: 15.5px;
    color: var(--ink);
  }
  .contact-list strong {
    font-weight: 700;
  }
  .contact-list.phones {
    width: 170px;
  }
</style>
</head>
<body>
  <main class="letterhead">
    <header class="brand">
      <span class="brand-mark"></span>
      <span class="brand-name">Meridian Systems</span>
    </header>

    <div class="footer-band" role="img" aria-label="Decorative blue flowing wave lines with soft orange bubbles"></div>

    <footer class="contact-panel">
      <ul class="contact-list phones">
        <li><strong>P:</strong> +61 2 9000 1234</li>
        <li><strong>F:</strong> +61 2 9000 5678</li>
        <li>www.meridiansystems.com.au</li>
        <li>info@meridiansystems.com.au</li>
      </ul>
      <ul class="contact-list address">
        <li>Level 7, 120 Harbour Street</li>
        <li>Sydnet, 2000</li>
        <li>Australia</li>
      </ul>
    </footer>
  </main>
</body>
</html>
```